Palisade Lift Inc Website Deisgn

We are a new small elevator contracting company.
We would like a full website designed similar to
http://brightmorelift.com or https://www.northpeaklifting.ca/
In addition to contents found on the above webpages.. we would like a section for project gallery etc.... have fun with it ... make it professional

Target Market(s)

Elevator Consultants - Property managers - Condo Boards - Commercial office buildings

Coding

Coded - Design and coding required

Number of Pages Required

5+ page

Requirements
Must have
• Navigation Bar.. Be view able via mobile ..Should be pictures of Tall Office buildings in background.. Toronto city skyline etc....

Have Fun!

```html
<!DOCTYPE html>
<html lang="en">
<head>
<meta charset="utf-8">
<title>Palisade Lift Inc</title>
<link rel="stylesheet" href="https://fonts.googleapis.com/css2?family=Oswald:wght@300;400;500;600&display=swap">
<style>
:root{
  --ink:#000;
  --paper:#fff;
  --blue:#0a74da;
  --grey-text:#555;
  --field:#eeeeee;
  --topbar-dark:#1a1a1a;
}
*{box-sizing:border-box;margin:0;padding:0}
html,body{width:1200px;height:3672px;overflow:hidden;background:var(--paper)}
body{position:relative;font-family:'Oswald',sans-serif;color:var(--ink)}
.abs{position:absolute}

.topbar{left:0;top:0;width:1200px;height:58px;background:var(--ink);color:#fff}
.topbar__welcome{left:66px;top:17px;font-size:17px;letter-spacing:1.5px;font-weight:400}
.topbar__social{left:800px;top:0;width:400px;height:58px;background:var(--topbar-dark);clip-path:polygon(30px 0,100% 0,100% 100%,0 100%)}
.topbar__follow{left:916px;top:16px;font-size:17px}
.dot{position:absolute;width:16px;height:16px;border-radius:50%;background:#fff}

.header{left:0;top:58px;width:1200px;height:152px;background:var(--paper)}
.brand{display:flex;align-items:center;gap:12px}
.brand__mark{width:56px;height:56px;border-radius:50%;border:6px solid var(--ink)}
.brand__name{font-size:40px;font-weight:600;letter-spacing:1px;color:var(--ink);line-height:1}
.nav{top:58px;font-size:23px;font-weight:400;color:var(--ink)}
.nav--active::after{content:"";position:absolute;left:4px;right:4px;top:45px;height:4px;background:var(--ink)}

.hero{left:0;top:210px;width:1200px;height:317px;background:linear-gradient(180deg,#6b6660 0%,#4b4a48 45%,#2e2d2b 100%)}
.hero__badge{left:578px;top:272px;width:44px;height:44px;border-radius:50%;border:4px solid #fff}
.hero__title{left:0;width:1200px;top:322px;text-align:center;color:#fff;font-size:56px;font-weight:600;line-height:1.1}
.hero__sub{left:0;width:1200px;top:388px;text-align:center;color:#fff;font-size:22px;font-weight:500;letter-spacing:5px}

.quote{left:67px;top:480px;width:1066px;height:304px;background:var(--blue);box-shadow:0 12px 20px rgba(0,0,0,.18)}
.quote__title{left:0;width:1066px;top:40px;text-align:center;color:#fff;font-size:36px;font-weight:500;letter-spacing:2px}
.field{height:47px;background:var(--paper);font-size:14px;color:#222;padding:14px 18px;font-weight:300}
.field--grey{background:var(--field)}
.field__arrow{position:absolute;right:16px;top:19px;width:0;height:0;border-left:6px solid transparent;border-right:6px solid transparent;border-top:10px solid #000}
.btn{display:flex;align-items:center;justify-content:center;color:#fff;font-size:14px;font-weight:600}
.btn--black{background:var(--ink)}
.btn--blue{background:var(--blue)}
.quote__note{left:0;width:1066px;top:196px;text-align:center;color:#fff;font-size:16px;line-height:26px;font-weight:400}

.welcome__eyebrow{left:66px;top:926px;font-size:17px;letter-spacing:1.5px}
.welcome__title{left:64px;top:954px;font-size:42px;font-weight:400}
.welcome__lead{left:66px;top:1022px;font-size:20px}
.welcome__text{left:66px;top:1052px;width:516px;font-size:14px;line-height:26px;color:var(--grey-text);font-weight:300}
.welcome__photo{left:644px;top:869px;width:456px;height:456px;border-radius:50%;background:radial-gradient(circle at 55% 45%,#9fc9c8,#557c80 55%,#2f3f46)}
.welcome__ring{left:636px;top:872px;width:470px;height:456px;border-radius:50%;border-left:10px solid var(--ink);border-top:6px solid var(--ink)}
.trust{left:635px;top:1178px;width:180px;height:180px;border-radius:50%;background:var(--ink);color:#fff;text-align:center;box-shadow:0 8px 14px rgba(0,0,0,.25)}
.trust__label{margin-top:52px;font-size:18px;letter-spacing:1px}
.trust__num{font-size:46px;line-height:1;font-weight:400}

.section-title{left:0;width:1200px;text-align:center;font-size:36px;font-weight:500;letter-spacing:3px}
.consult__sub{left:150px;width:900px;top:1508px;text-align:center;font-size:21px;line-height:31px;color:#444;font-weight:300}
.card__photo{top:1607px;width:329px;height:274px}
.card__body{top:1881px;width:304px;height:171px;background:var(--ink);color:#fff}
.card__title{position:absolute;left:22px;top:26px;font-size:24px}
.card__text{position:absolute;left:22px;top:76px;width:260px;font-size:12px;line-height:19px;color:#bbb;font-weight:300}
.card__btn{top:2029px;width:192px;height:47px}

.projects{left:0;top:2239px;width:1200px;height:696px;background:var(--ink)}
.slide{top:2377px;height:433px}
.slide__cap{top:2672px;width:305px;height:124px;background:rgba(0,0,0,.85);color:#fff;text-align:center}
.slide__title{margin-top:20px;font-size:24px}
.slide__text{margin:10px auto 0;width:250px;font-size:12px;line-height:19px;color:#aaa;font-weight:300}

.map{left:0;top:2935px;width:1200px;height:280px;background:linear-gradient(90deg,#d4d4d4,#e2e2e2 50%,#d6d6d6)}
.form{left:67px;top:3139px;width:1066px;height:372px;background:var(--paper)}

.footer{left:0;top:3511px;width:1200px;height:161px;background:var(--ink);color:#fff}
.footer .brand__mark{border-color:#fff;width:46px;height:46px;border-width:5px}
.footer .brand__name{color:#fff;font-size:30px}
.footer__copy{left:440px;top:3583px;font-size:12px;color:#888;font-weight:300}
.footer__icon{width:30px;height:30px;border-radius:50%;background:#fff}
</style>
</head>
<body>

<div class="abs topbar">
  <div class="abs topbar__welcome">WELCOME TO ELEVATOR SERVICE SPECIALISTS</div>
  <div class="abs topbar__social"></div>
  <div class="abs topbar__follow">Follow us</div>
  <span class="dot" style="left:1012px;top:21px"></span>
  <span class="dot" style="left:1055px;top:21px"></span>
  <span class="dot" style="left:1100px;top:21px"></span>
</div>

<header class="abs header">
  <div class="abs brand" style="left:66px;top:46px">
    <span class="brand__mark"></span>
    <span class="brand__name">PALISADE LIFT INC</span>
  </div>
  <span class="abs nav nav--active" style="left:614px">Home</span>
  <span class="abs nav" style="left:704px">About</span>
  <span class="abs nav" style="left:794px">Services</span>
  <span class="abs nav" style="left:914px">Consultants</span>
  <span class="abs nav" style="left:1064px">Contact</span>
</header>

<section class="abs hero" role="img" aria-label="Aerial photo of the Toronto skyline with a tall tower and office buildings"></section>
<div class="abs hero__badge"></div>
<h1 class="abs hero__title">WE ARE TORONTO’S #1</h1>
<p class="abs hero__sub">CHOICE FOR ELEVATOR MAINTENANCE, REPAIR AND MODERNIZATION</p>

<section class="abs quote">
  <h2 class="abs quote__title">GET OUR FREE QUOTE</h2>
  <div class="abs field" style="left:41px;top:119px;width:250px">Your name</div>
  <div class="abs field" style="left:304px;top:119px;width:250px">Phone Number</div>
  <div class="abs field" style="left:566px;top:119px;width:250px">Type of Service<span class="field__arrow"></span></div>
  <div class="abs btn btn--black" style="left:829px;top:119px;width:193px;height:47px">Get A Quote</div>
  <p class="abs quote__note">For Business inquiry fill below from or call toll free num - (+88) 02-555-0147.<br>Our team will contact you shortly</p>
</section>

<section>
  <div class="abs welcome__eyebrow">WELCOME TO</div>
  <h2 class="abs welcome__title">Palisade Lift Inc</h2>
  <div class="abs welcome__lead">Running a Successful Business Since 1982</div>
  <p class="abs welcome__text">There are many variations of passages of Lorem Ipsum available, but the majority have suffered alteration in some form, by injected humour, or randomised words which don't look even slightly believable. You need to be sure there isn't anything embarrassing hidden in the middle of text. All the lorem ipsum generators on the Internet....</p>
  <div class="abs btn btn--blue" style="left:66px;top:1196px;width:193px;height:47px">Learn more</div>
  <div class="abs welcome__ring"></div>
  <div class="abs welcome__photo" role="img" aria-label="Looking down an elevator shaft at two technicians in hard hats working on the car roof"></div>
  <div class="abs trust"><div class="trust__label">TRUSTED BY</div><div class="trust__num">566+</div></div>
</section>

<section>
  <h2 class="abs section-title" style="top:1458px">CONSULTANTS TO MODERIZATION</h2>
  <p class="abs consult__sub">Offering a number of different services including&nbsp; Elevator Consultants - Property managers - Condo Boards - Commercial office buildings</p>

  <div class="abs card__photo" style="left:67px;background:linear-gradient(135deg,#cfe3f2,#7d93a8 60%,#2f3a48)" role="img" aria-label="Two consultants in orange hard hats reviewing plans in a glass building"></div>
  <div class="abs card__body" style="left:67px"><div class="card__title">Elevator Consultants</div><div class="card__text">Incididunt ut labore et dolore magna aliqua. Ut exercitation ullamco laboris nisi ut aliquip ex ea ....</div></div>
  <div class="abs btn btn--blue card__btn" style="left:67px">Learn more</div>

  <div class="abs card__photo" style="left:436px;background:linear-gradient(135deg,#e0e4ea,#8a9bb5 55%,#3e4a5c)" role="img" aria-label="Two technicians in white hard hats servicing elevator machinery"></div>
  <div class="abs card__body" style="left:436px"><div class="card__title">Maintaince</div><div class="card__text">Incididunt ut labore et dolore magna aliqua. Ut exercitation ullamco laboris nisi ut aliquip ex ea ....</div></div>
  <div class="abs btn btn--black card__btn" style="left:436px">Learn more</div>

  <div class="abs card__photo" style="left:805px;background:linear-gradient(135deg,#c99a2e,#5e4a2a 50%,#6e7278)" role="img" aria-label="Technician with an open toolbox beside elevator equipment"></div>
  <div class="abs card__body" style="left:805px"><div class="card__title">Service &amp; Repair</div><div class="card__text">Incididunt ut labore et dolore magna aliqua. Ut exercitation ullamco laboris nisi ut aliquip ex ea ....</div></div>
  <div class="abs btn btn--black card__btn" style="left:805px">Learn more</div>
</section>

<section class="abs projects"></section>
<h2 class="abs section-title" style="top:2291px;color:#fff">OUR PROJECTS</h2>
<div class="abs slide" style="left:0;width:43px;background:linear-gradient(90deg,#3a4250,#6a7280)" role="img" aria-label="Edge of a previous project photo"></div>
<div class="abs slide" style="left:67px;width:434px;background:linear-gradient(135deg,#8d8d8d,#c2c2c2 40%,#5a5a5a)" role="img" aria-label="Stainless steel elevator panel with call buttons and a touch screen"></div>
<div class="abs slide__cap" style="left:131px"><div class="slide__title">Ontario Eleavtor</div><div class="slide__text">Incididunt ut labore et dolore magna aliqua. Ut exercitation ullamco laboris nisi ut aliquip ex ea ....</div></div>
<div class="abs slide" style="left:527px;width:433px;background:linear-gradient(90deg,#dcdcdc,#3a3d44 40%,#22252a 60%,#d0d0d0)" role="img" aria-label="Glass elevator shafts rising through a multi-storey atrium"></div>
<div class="abs slide__cap" style="left:592px"><div class="slide__title">Elevator Atrium on Bay</div><div class="slide__text">Incididunt ut labore et dolore magna aliqua. Ut exercitation ullamco laboris nisi ut aliquip ex ea ....</div></div>
<div class="abs slide" style="left:986px;width:214px;background:linear-gradient(135deg,#2f3a4e,#6c7a8e 60%,#b6bcc4)" role="img" aria-label="Close-up of numbered elevator buttons"></div>
<div class="abs slide__cap" style="left:1051px;width:149px;text-align:left;overflow:hidden"><div class="slide__title" style="padding-left:82px;white-space:nowrap">Ontario</div><div class="slide__text" style="margin-left:38px;width:250px;text-align:left">Incididunt ut labore et<br>exercitation ullamco lab</div></div>
<div class="abs btn btn--blue" style="left:504px;top:2844px;width:193px;height:46px">See All</div>

<div class="abs map" role="img" aria-label="Street map of downtown Toronto around Yonge Street and Cabbagetown"></div>
<section class="abs form">
  <h2 class="abs section-title" style="top:30px;width:1066px">FREE QUOTE</h2>
  <div class="abs field field--grey" style="left:147px;top:97px;width:251px">Your name</div>
  <div class="abs field field--grey" style="left:409px;top:97px;width:251px">Phone Number</div>
  <div class="abs field field--grey" style="left:671px;top:97px;width:251px">Type of Service<span class="field__arrow"></span></div>
  <div class="abs field field--grey" style="left:147px;top:164px;width:775px;height:93px">Message...</div>
  <div class="abs btn btn--blue" style="left:144px;top:287px;width:778px;height:47px">Get A Quote</div>
</section>

<footer class="abs footer">
  <div class="abs brand" style="left:66px;top:50px;gap:10px">
    <span class="brand__mark"></span>
    <span class="brand__name">PALISADE LIFT INC</span>
  </div>
</footer>
<div class="abs footer__copy">© Copyrights 2020 Palisade Lift Inc. All rights reserved</div>
<span class="abs footer__icon" style="left:947px;top:3576px"></span>
<span class="abs footer__icon" style="left:1017px;top:3576px"></span>
<span class="abs footer__icon" style="left:1093px;top:3576px"></span>

</body>
</html>
```